Criminal Defense Firm looking for an edge in business card design

Established Criminal Defense Firm looking to refresh business card. We already have logo and website, but our business cards are extremely boring. We would like to also have something on the backside of card.
Needs to be business oriented, but creative.
We provide services to professionals such as doctors, lawyers, politicians, etc.
Our specialty is to protect professional licenses when facing a criminal matter.

Update on March 10, 2015: This project is for a Business Card Design. The winner in this project will be assigned the next (1on1) project which incidentally is also entitled Business Card Design. I'm sorry for this confusion. The 1on1 project will not be for Business Card Design but will be for Stationery-Envelope Design. Thank you for your attention and continued participation.

Target Market(s)

People accused of a crime

Industry/Entity Type

Business

Contact Information for Business Card

Simple, strong, professional

Colors
85abd2
3176b5
0355a3

```html
<!DOCTYPE html>
<html lang="en">
<head>
<meta charset="utf-8">
<title>Whitcombe Ashford Law Corporation — Business Cards</title>
<link href="https://fonts.googleapis.com/css2?family=Lato:wght@400;700;900&display=swap" rel="stylesheet">
<style>
  :root {
    --backdrop: #dfe2e1;
    --card: #ffffff;
    --card-shade: #eceef0;
    --navy: #0d3a63;
    --brand-blue: #3176b5;
    --brand-light: #85abd2;
    --ink: #1f2326;
    --ink-soft: #3a3f44;
    --faint: #e3e5e8;
    --on-navy: #e8eef5;
  }
  * { box-sizing: border-box; margin: 0; padding: 0; }
  html, body { width: 1200px; height: 900px; overflow: hidden; }
  body {
    background: var(--backdrop);
    font-family: "Lato", Arial, sans-serif;
    position: relative;
  }
  .card {
    position: absolute;
    width: 560px;
    height: 320px;
    background: linear-gradient(180deg, var(--card) 0%, var(--card) 55%, var(--card-shade) 100%);
    box-shadow: 0 14px 30px rgba(0,0,0,0.28);
    overflow: hidden;
  }
  .card--back { left: 70px; top: 70px; }
  .card--front { left: 570px; top: 500px; }

  .faint-mark {
    position: absolute;
    border-radius: 50%;
    border: 3px solid var(--faint);
    background: rgba(227,229,232,0.45);
  }
  .card--back .faint-mark { width: 120px; height: 120px; right: 40px; top: 30px; }
  .card--front .faint-mark {
    width: 110px; height: 110px; right: 22px; top: 104px; z-index: 2;
    border-color: rgba(255,255,255,0.65); background: rgba(214,219,224,0.55);
  }

  .brand {
    position: absolute;
    left: 60px; bottom: 70px;
    display: flex; align-items: center; gap: 16px;
  }
  .brand__dot {
    width: 62px; height: 62px; border-radius: 50%;
    background: var(--brand-blue);
    flex: none;
  }
  .brand__name {
    font-size: 26px; font-weight: 700; color: var(--brand-blue);
    line-height: 1.05; letter-spacing: 0.5px;
  }
  .brand__name span { display: block; }

  .person {
    position: absolute; top: 84px; left: 0; right: 120px;
    text-align: center;
  }
  .person__name { font-size: 27px; font-weight: 900; color: var(--ink); }
  .person__title { font-size: 17px; color: var(--ink-soft); letter-spacing: 1px; margin-top: 4px; }

  .band { position: absolute; left: 0; top: 0; width: 560px; height: 320px; z-index: 1; }

  .address {
    position: absolute; left: 30px; top: 194px; z-index: 3;
    font-size: 15px; color: var(--ink); white-space: nowrap;
  }
  .contact { position: absolute; z-index: 3; list-style: none; color: var(--on-navy); }
  .contact li { display: flex; align-items: center; gap: 10px; height: 22px; white-space: nowrap; }
  .contact svg { width: 16px; height: 16px; flex: none; }
  .contact--phones { left: 34px; top: 264px; font-size: 16px; }
  .contact--online { left: 288px; top: 228px; font-size: 14px; }
</style>
</head>
<body>

  <section class="card card--back" aria-label="Card back">
    <div class="faint-mark" aria-hidden="true"></div>
    <div class="brand">
      <div class="brand__dot" aria-hidden="true"></div>
      <p class="brand__name"><span>Whitcombe Ashford</span><span>Law Corporation</span></p>
    </div>
  </section>

  <section class="card card--front" aria-label="Card front">
    <svg class="band" viewBox="0 0 560 320" aria-hidden="true">
      <path d="M0 252 H250 Q262 252 266 240 L270 228 Q274 218 288 218 H446 Q458 218 464 208 L468 200 Q472 190 484 190 H560 V320 H0 Z" fill="var(--navy)"/>
      <path d="M446 218 Q458 218 464 208 L468 200 Q472 190 484 190 H560 V202 H490 Q478 202 474 210 Z" fill="var(--brand-blue)" opacity="0.35"/>
    </svg>
    <div class="faint-mark" aria-hidden="true"></div>

    <div class="person">
      <h1 class="person__name">Daniel Whitcombe</h1>
      <p class="person__title">ATTORNEY AT LAW</p>
    </div>

    <p class="address">1870 Lindell Avenue Suite 210 Clearview, CA 90210</p>

    <ul class="contact contact--online">
      <li>
        <svg viewBox="0 0 16 16"><rect x="1" y="3" width="14" height="10" fill="none" stroke="currentColor" stroke-width="1.5"/><path d="M1 3 L8 9 L15 3" fill="none" stroke="currentColor" stroke-width="1.5"/></svg>
        daniel@wacriminaldefense.com
      </li>
      <li>
        <svg viewBox="0 0 16 16"><rect x="1" y="2" width="14" height="9" fill="none" stroke="currentColor" stroke-width="1.5"/><path d="M5 14 H11 M8 11 V14" stroke="currentColor" stroke-width="1.5"/></svg>
        www.wacriminaldefense.com
      </li>
    </ul>

    <ul class="contact contact--phones">
      <li>
        <svg viewBox="0 0 16 16"><path d="M2 6 Q8 1 14 6 L12 8 L10 6.5 L6 6.5 L4 8 Z" fill="currentColor"/><rect x="4" y="9" width="8" height="5" rx="1" fill="currentColor"/></svg>
        555-014-2200
      </li>
      <li>
        <svg viewBox="0 0 16 16"><rect x="4" y="1" width="8" height="4" fill="currentColor"/><rect x="1" y="6" width="14" height="6" rx="1" fill="currentColor"/><rect x="4" y="10" width="8" height="5" fill="var(--on-navy)" stroke="var(--navy)" stroke-width="1"/></svg>
        555-014-2201
      </li>
    </ul>
  </section>

</body>
</html>
```